Online Marketing Agency Website

We are an online marketing agency that specializes in search marketing (SEM) for businesses of all sizes. Our core services include local search marketing, seo, paid search, paid social, graphic design, video production/editing and website design. We have an existing website that we launched a number of years ago but it's very outdated and we're currently too busy to design a new version.

Target Market(s)

Any business that needs online marketing services with an emphasis on search marketing.

Industry/Entity Type

Ad Agency

Number of Pages Required

4 page

Font styles to use
Sans Serif

Requirements
Must have
• Home page, interior page, blog page, contact us page.
Look and feel should be modern and clean and easy to navigate.
Sections for call outs for specific services: Business Marketing Strategy, Content Creation and Marketing, Graphic & Publication Design, Pay Per Click (PPC) Management, Search Engine Optimization, Social Media Management, Video Production & Editing, Website Hosting & Management, Website Design & Development
Use color from logo that was uploaded.

```html
<!DOCTYPE html>
<html lang="en">
<head>
<meta charset="utf-8">
<title>Northpeak Media — Blog</title>
<link href="https://fonts.googleapis.com/css2?family=Exo+2:wght@400;500;700&display=swap" rel="stylesheet">
<style>
:root{
  --dark:#4a4a4a;
  --orange:#ff4a12;
  --ink:#2b2b2b;
  --card:#f1f2f4;
  --line:#e2e3e6;
  --white:#ffffff;
  --field:#d9d9d9;
}
*{margin:0;padding:0;box-sizing:border-box}
html,body{width:763px;height:1200px;overflow:hidden;background:var(--white)}
body{position:relative;font-family:"Exo 2",sans-serif;color:var(--ink)}
.site-header{position:absolute;left:0;top:0;width:763px;height:83px;background:var(--dark)}
.brand{position:absolute;display:flex;align-items:center;gap:5px;color:var(--white);font-weight:500;font-size:9px;white-space:nowrap}
.brand-dot{width:10px;height:10px;border-radius:50%;background:var(--orange)}
.nav a{position:absolute;top:25px;font-size:6.8px;color:var(--white);text-decoration:none;white-space:nowrap}
.nav a.active{color:var(--orange)}
.nav .caret{display:inline-block;vertical-align:middle;margin-left:2px}
.cta{position:absolute;left:538px;top:20px;width:82px;height:18px;border-radius:9px;background:var(--orange);color:var(--white);font-size:6.8px;font-weight:500;display:flex;align-items:center;justify-content:center}
.page-title{position:absolute;left:0;width:763px;top:122px;text-align:center;font-size:14px;font-weight:700}
.back{position:absolute;left:345px;top:146px;font-size:6.5px;display:flex;align-items:center;gap:5px}
.cats a{position:absolute;top:180px;font-size:6.8px;color:var(--orange);text-decoration:none}
.post{position:absolute;width:472px;height:118px;background:var(--card);border:0.5px solid var(--line)}
.post-media{position:absolute;left:0;top:0;width:149px;height:118px}
.m-hand{background:linear-gradient(120deg,#f3efe8 0%,#e4d6bf 45%,#c7ad8e 70%,#efece7 100%)}
.m-office{background:linear-gradient(180deg,#e9e9e7 0%,#cfd0cd 45%,#6f706c 75%,#3e3f3d 100%)}
.m-medal{background:linear-gradient(135deg,#e8e9ee 0%,#e33a2c 35%,#f4f4f6 50%,#2a2740 65%,#d8b23a 85%,#eef0f3 100%)}
.post-date{position:absolute;left:177px;top:31px;font-size:6.5px}
.post-cat{position:absolute;right:27px;top:31px;font-size:6.5px;color:var(--orange)}
.post-title{position:absolute;left:177px;top:48px;display:flex;align-items:center;gap:6px;font-size:8.3px;font-weight:400;white-space:nowrap}
.post-body{position:absolute;left:177px;top:69px;width:258px;font-size:6.4px;line-height:8.3px}
.more{position:absolute;left:354px;top:1006px;width:56px;height:18px;border:0.8px solid var(--orange);border-radius:9px;color:var(--orange);font-size:6.8px;display:flex;align-items:center;justify-content:center}
.site-footer{position:absolute;left:0;top:1055px;width:763px;height:145px;background:var(--dark);color:var(--white)}
.f-links{position:absolute;top:24px;list-style:none;font-size:5.7px;line-height:12px}
.f-head{position:absolute;left:508px;top:25px;font-size:8.5px}
.f-sub{position:absolute;left:508px;top:46px;font-size:5.7px}
.field{position:absolute;left:508px;width:108px;height:17px;border-radius:8.5px;background:var(--field);color:var(--white);font-size:5.7px;padding-left:9px;display:flex;align-items:center}
.send{position:absolute;left:581px;top:103px;width:36px;height:18px;border-radius:9px;background:var(--orange);font-size:6px;display:flex;align-items:center;justify-content:center}
.social{position:absolute;top:103px;width:18px;height:18px;border-radius:50%;border:0.8px solid #8a8a8a}
.copy{position:absolute;left:267px;top:116px;font-size:5.7px}
</style>
</head>
<body>
<header class="site-header">
  <div class="brand" style="left:146px;top:35px"><span class="brand-dot"></span>Northpeak Media</div>
  <nav class="nav">
    <a style="left:287px">SERVICES<svg class="caret" width="6" height="4" viewBox="0 0 6 4"><path d="M.5.5 3 3 5.5.5" fill="none" stroke="#fff" stroke-width=".8"/></svg></a>
    <a style="left:338px">FEATURED WORK</a>
    <a style="left:410px">ABOUT</a>
    <a class="active" style="left:446px">BLOG</a>
    <a style="left:480px">CONTACT US</a>
  </nav>
  <div class="cta">FREE CONSULTATION</div>
</header>

<h1 class="page-title">Blog</h1>
<div class="back"><svg width="11" height="7" viewBox="0 0 11 7"><path d="M10.5 3.5H1M4 .5 1 3.5 4 6.5" fill="none" stroke="#2b2b2b" stroke-width=".8"/></svg>Back to Main Page</div>
<nav class="cats">
  <a style="left:296px">News</a><a style="left:329px">Studio Life</a><a style="left:377px">Awards</a><a style="left:416px">Support</a><a style="left:457px">Tag</a>
</nav>

<main>
  <article class="post" style="left:146px;top:220px">
    <div class="post-media m-hand" role="img" aria-label="Photo of two people shaking hands over a desk"></div>
    <span class="post-date">Jul 12, 2020</span><span class="post-cat">News</span>
    <h2 class="post-title"><svg width="20" height="14" viewBox="0 0 20 14"><path d="M0 7h19M12.5.5 19 7l-6.5 6.5" fill="none" stroke="#ff4a12" stroke-width="1.2"/></svg>Northpeak camp: available for everyone from now!</h2>
    <p class="post-body">Lorem ipsum dolor sit amet, consectetur adipiscing elit, sed do eiusmod tempor incididunt ut labore et dolore magna aliqua. Ut enim ad minim veniam, quis nostrud exercitation ullamco laboris nisi</p>
  </article>
  <article class="post" style="left:145px;top:351px">
    <div class="post-media m-office" role="img" aria-label="Photo of a bright open-plan office with plants"></div>
    <span class="post-date">Jul 12, 2020</span><span class="post-cat">Studio Life</span>
    <h2 class="post-title"><svg width="20" height="14" viewBox="0 0 20 14"><path d="M0 7h19M12.5.5 19 7l-6.5 6.5" fill="none" stroke="#ff4a12" stroke-width="1.2"/></svg>We opened new office in Seattle!</h2>
    <p class="post-body">Lorem ipsum dolor sit amet, consectetur adipiscing elit, sed do eiusmod tempor incididunt ut labore et dolore magna aliqua. Ut enim ad minim veniam, quis nostrud exercitation ullamco laboris nisi</p>
  </article>
  <article class="post" style="left:145px;top:483px">
    <div class="post-media m-medal" role="img" aria-label="Photo of a gold medal on a striped ribbon"></div>
    <span class="post-date">Jul 12, 2020</span><span class="post-cat">Awards</span>
    <h2 class="post-title"><svg width="20" height="14" viewBox="0 0 20 14"><path d="M0 7h19M12.5.5 19 7l-6.5 6.5" fill="none" stroke="#ff4a12" stroke-width="1.2"/></svg>We won „Best Website” Award by WebShowcase. Happy to share it.</h2>
    <p class="post-body">Lorem ipsum dolor sit amet, consectetur adipiscing elit, sed do eiusmod tempor incididunt ut labore et dolore magna aliqua. Ut enim ad minim veniam, quis nostrud exercitation ullamco laboris nisi</p>
  </article>
  <article class="post" style="left:145px;top:616px">
    <div class="post-media m-hand" role="img" aria-label="Photo of two people shaking hands over a desk"></div>
    <span class="post-date">Jul 12, 2020</span><span class="post-cat">News</span>
    <h2 class="post-title"><svg width="20" height="14" viewBox="0 0 20 14"><path d="M0 7h19M12.5.5 19 7l-6.5 6.5" fill="none" stroke="#ff4a12" stroke-width="1.2"/></svg>Northpeak camp: available for everyone from now!</h2>
    <p class="post-body">Lorem ipsum dolor sit amet, consectetur adipiscing elit, sed do eiusmod tempor incididunt ut labore et dolore magna aliqua. Ut enim ad minim veniam, quis nostrud exercitation ullamco laboris nisi</p>
  </article>
  <article class="post" style="left:143px;top:747px">
    <div class="post-media m-office" role="img" aria-label="Photo of a bright open-plan office with plants"></div>
    <span class="post-date">Jul 12, 2020</span><span class="post-cat">Studio Life</span>
    <h2 class="post-title"><svg width="20" height="14" viewBox="0 0 20 14"><path d="M0 7h19M12.5.5 19 7l-6.5 6.5" fill="none" stroke="#ff4a12" stroke-width="1.2"/></svg>We opened new office in Seattle!</h2>
    <p class="post-body">Lorem ipsum dolor sit amet, consectetur adipiscing elit, sed do eiusmod tempor incididunt ut labore et dolore magna aliqua. Ut enim ad minim veniam, quis nostrud exercitation ullamco laboris nisi</p>
  </article>
  <article class="post" style="left:143px;top:879px">
    <div class="post-media m-medal" role="img" aria-label="Photo of a gold medal on a striped ribbon"></div>
    <span class="post-date">Jul 12, 2020</span><span class="post-cat">Awards</span>
    <h2 class="post-title"><svg width="20" height="14" viewBox="0 0 20 14"><path d="M0 7h19M12.5.5 19 7l-6.5 6.5" fill="none" stroke="#ff4a12" stroke-width="1.2"/></svg>We won „Best Website” Award by WebShowcase. Happy to share it.</h2>
    <p class="post-body">Lorem ipsum dolor sit amet, consectetur adipiscing elit, sed do eiusmod tempor incididunt ut labore et dolore magna aliqua. Ut enim ad minim veniam, quis nostrud exercitation ullamco laboris nisi</p>
  </article>
  <div class="more">Show more</div>
</main>

<footer class="site-footer">
  <div class="brand" style="left:146px;top:30px"><span class="brand-dot"></span>Northpeak Media</div>
  <ul class="f-links" style="left:267px">
    <li>Business Marketing Strategy</li><li>Content Creation and Marketing,</li><li>Graphic &amp; Publication Design</li><li>Pay Per Click (PPC) Management</li><li>Search Engine Optimization</li>
  </ul>
  <ul class="f-links" style="left:383px">
    <li>Social Media Management</li><li>Video Production &amp; Editing</li><li>Website Hosting &amp; Management</li><li>Website Design &amp; Development</li>
  </ul>
  <div class="f-head">Stay in touch!</div>
  <div class="f-sub">Subscrive to our newsletter</div>
  <div class="field" style="top:57px">Name</div>
  <div class="field" style="top:78px">E-mail</div>
  <div class="send">Send</div>
  <span class="social" style="left:145px"></span>
  <span class="social" style="left:171px"></span>
  <span class="social" style="left:197px"></span>
  <span class="social" style="left:223px"></span>
  <div class="copy">© Northpeak Media. 2020. All rights reserved.</div>
</footer>
</body>
</html>
```